Design refresh required for educational resources

A full redesign/refresh is required for an education resource kit.
The final outputs will include:
- Powerpoint slide template
- parent handout template
- overview template
- 2 different types of lesson plan templates (can be related but need to have some differences to distinguish between the two)
- 2 x branded labels for resources
- teacher 'intervention plan' summary sheet
- 'scope and sequence' document
Design needs to have a fun, modern feel, capturing elements of the New Zealand landscape, flora and/or fauna.
The resources will be used as part of a teaching kit for use in schools.
Please see attached files for existing samples of some of the above documents. Full content to be provided for successful applicant.
Please submit sample of one or two of the documents to bid for this work - enough so that I can see the overall design aesthetic you are proposing.
New Zealand teachers and parents of 5 year old children

```html
<!DOCTYPE html>
<html lang="en">
<head>
<meta charset="utf-8">
<title>Week 1 Parent Overview</title>
<link rel="stylesheet" href="https://fonts.googleapis.com/css2?family=Open+Sans:ital,wght@0,600;0,700;0,800;1,700&family=Source+Sans+3:wght@400;600;700&family=Luckiest+Guy&display=swap">
<style>
  :root {
    --purple: #4a2d82;
    --purple-deep: #3b2470;
    --green: #7dc24b;
    --green-bright: #8cc63f;
    --grey-band: #dedde3;
    --grey-line: #b9b8bf;
    --text: #3c3c3c;
    --white: #ffffff;
  }
  * { box-sizing: border-box; margin: 0; padding: 0; }
  html, body { width: 921px; height: 1200px; overflow: hidden; background: var(--white); }
  body { font-family: "Source Sans 3", sans-serif; color: var(--text); position: relative; }

  .header {
    position: absolute; left: 0; top: 0; width: 921px; height: 317px;
    background: linear-gradient(180deg, var(--purple) 0%, var(--purple-deep) 100%);
    overflow: hidden;
  }
  .header-stripe { position: absolute; left: 0; top: 317px; width: 921px; height: 14px; background: var(--green-bright); }

  .week-badge { position: absolute; left: 56px; top: 0; width: 240px; height: 120px; }
  .week-label {
    position: absolute; left: 106px; top: 22px; width: 134px; height: 56px;
    display: flex; align-items: flex-end; gap: 4px;
    font-family: "Luckiest Guy", "Open Sans", sans-serif; font-weight: 800;
    color: var(--purple); line-height: 1;
    text-shadow: -1px -1px 0 #fff, 1px -1px 0 #fff, -1px 1px 0 #fff, 1px 1px 0 #fff;
  }
  .week-label .word { font-size: 30px; letter-spacing: 0.5px; }
  .week-label .num { font-size: 46px; }

  .headline {
    position: absolute; left: 70px; top: 136px;
    font-family: "Open Sans", sans-serif; font-weight: 700; font-size: 34px; line-height: 42px;
    color: var(--green); text-transform: uppercase; letter-spacing: -0.3px;
  }
  .book-title {
    position: absolute; left: 71px; top: 228px;
    font-family: "Open Sans", sans-serif; font-weight: 700; font-style: italic; font-size: 20px; color: var(--white);
  }
  .book-authors { position: absolute; left: 71px; top: 256px; font-size: 19px; color: var(--white); }

  .book-cover {
    position: absolute; left: 594px; top: 46px; width: 250px; height: 256px;
    border: 1px solid #cfd6ee;
    background: linear-gradient(180deg, #f2b98a 0%, #e9a0a8 35%, #6aa3d6 62%, #2f63b3 100%);
  }

  .section { position: absolute; left: 69px; width: 778px; }
  .section-icon {
    position: absolute; left: 0; top: 0; width: 67px; height: 67px;
    background: var(--green-bright); border-radius: 8px;
  }
  .section-icon svg { width: 67px; height: 67px; display: block; }
  .section-box {
    position: absolute; left: 79px; top: 0; width: 699px;
    border: 1px solid var(--grey-line); border-radius: 9px; overflow: hidden; background: var(--white);
  }
  .section-title {
    background: var(--grey-band); padding: 4px 15px 3px;
    font-family: "Open Sans", sans-serif; font-weight: 600; font-size: 19px; color: var(--purple);
    text-transform: uppercase; letter-spacing: -0.2px;
  }
  .section-body { padding: 6px 12px 12px; font-size: 17px; line-height: 25px; }
  .section-body .term { color: var(--purple); font-weight: 600; }

  .sounds .section-body { padding-top: 10px; line-height: 28px; }

  .ideas-list { list-style: none; padding: 8px 18px 10px 12px; font-size: 16.5px; line-height: 22.5px; }
  .ideas-list li { position: relative; padding-left: 17px; margin-bottom: 5px; }
  .ideas-list li::before {
    content: ""; position: absolute; left: 1px; top: 10px; width: 4px; height: 4px;
    border-radius: 50%; background: var(--purple);
  }

  .footer-note { position: absolute; left: 66px; top: 1130px; font-size: 16px; line-height: 21px; }
  .footer-note .link { color: var(--purple); font-weight: 700; }
  .footer-rule { position: absolute; left: 63px; top: 1180px; width: 540px; height: 1px; background: #d8d8d8; }

  .partners { position: absolute; left: 630px; top: 1128px; height: 60px; display: flex; align-items: center; }
  .partner { display: flex; align-items: center; gap: 7px; font-size: 14px; font-weight: 700; color: var(--purple); line-height: 16px; }
  .partner-mark { width: 16px; height: 16px; background: var(--green); flex: none; }
  .partner-divider { width: 1px; height: 56px; background: #555; margin: 0 12px; }
</style>
</head>
<body>
  <header class="header">
    <svg class="week-badge" viewBox="0 0 240 120" aria-hidden="true">
      <circle cx="116" cy="-6" r="114" fill="none" stroke="#ffffff" stroke-width="1.5"/>
      <circle cx="116" cy="-8" r="106" fill="#7dc24b"/>
    </svg>
    <div class="week-label"><span class="word">WEEK</span><span class="num">1</span></div>

    <h1 class="headline">This week your<br>child’s class is reading</h1>
    <p class="book-title">Captain Puddle on the Rolling Waves</p>
    <p class="book-authors">By Harriet Lowe and Mina Cole</p>

    <div class="book-cover" role="img" aria-label="Book cover artwork"></div>
  </header>
  <div class="header-stripe"></div>

  <section class="section words" style="top:382px;">
    <div class="section-icon">
      <svg viewBox="0 0 67 67" aria-hidden="true">
        <circle cx="33.5" cy="17" r="6" fill="#fff"/>
        <path d="M22 27h23v6H22z" fill="#fff"/>
        <path d="M17 35l16 4v15l-16-4z M50 35l-16 4v15l16-4z" fill="#fff"/>
      </svg>
    </div>
    <div class="section-box">
      <h2 class="section-title">Some new words your child is learning</h2>
      <div class="section-body">
        <p><span class="term">Brave</span> means to be ready to face danger and be courageous.</p>
        <p><span class="term">Depart</span> is when somebody goes away or leaves.</p>
        <p>A <span class="term">breeze</span> is a very light wind.</p>
        <p><span class="term">Hoist</span> means to lift or haul something up using a mechanical device.</p>
      </div>
    </div>
  </section>

  <section class="section sounds" style="top:545px;">
    <div class="section-icon">
      <svg viewBox="0 0 67 67" aria-hidden="true">
        <path d="M16 28h9l12-10v31L25 39h-9z" fill="#fff"/>
        <path d="M42 27q5 6.5 0 13" stroke="#fff" stroke-width="3.5" fill="none" stroke-linecap="round"/>
        <path d="M47 22q9 11.5 0 23" stroke="#fff" stroke-width="3.5" fill="none" stroke-linecap="round"/>
      </svg>
    </div>
    <div class="section-box">
      <h2 class="section-title">Some new sounds your child is learning</h2>
      <div class="section-body">
        <p>'m' as in mud, man and moon</p>
        <p>'d' as in duck and dog</p>
      </div>
    </div>
  </section>

  <section class="section ideas" style="top:672px;">
    <div class="section-icon">
      <svg viewBox="0 0 67 67" aria-hidden="true">
        <g fill="none" stroke="#fff" stroke-width="3">
          <circle cx="33.5" cy="33.5" r="10"/>
          <circle cx="20" cy="16" r="4"/><circle cx="47" cy="16" r="4"/>
          <circle cx="20" cy="51" r="4"/><circle cx="47" cy="51" r="4"/>
          <path d="M12 26q-2 7.5 0 15 M55 26q2 7.5 0 15"/>
        </g>
      </svg>
    </div>
    <div class="section-box">
      <h2 class="section-title">Some fun ways you can play with sounds at home</h2>
      <ul class="ideas-list">
        <li>Use playdough, modelling clay, pipe cleaners or even blocks to make the shapes of this week's letters. Practice making the 'm' sound while you're creating your letters.</li>
        <li>Talk about how the letter looks, and then brainstorm some words that start with its sound. Your child may remember some of the words from class to start you off! When your child finds a word encourage them to say the name and the letter sound e.g. mug starts with an 'm' sound.</li>
        <li>Write the letters and have them around your home – draw your child's attention to them every time you see them and practice the sound.</li>
        <li>Hide objects or toys that start with the same letter as the one you are targeting and go on a 'letter' treasure hunt – see who can get the most of each letter. When they find them get them to yell out the sound!</li>
        <li>If you are reading a book with them see who can find any words that start with a 'm' or a 'd' the fastest. If they are able to, get them to read the word aloud, or support them in doing this. Practice making the 'm' or 'd' sound.</li>
      </ul>
    </div>
  </section>

  <footer>
    <p class="footer-note">To access online versions of the small readers visit<br>
      <span class="link">https://www.brightstepsreading.example/for-families</span></p>
    <div class="footer-rule"></div>
    <div class="partners">
      <div class="partner"><span class="partner-mark"></span><span>Bright Steps<br>Reading</span></div>
      <div class="partner-divider"></div>
      <div class="partner"><span>Kōwhai Valley<br>University</span></div>
    </div>
  </footer>
</body>
</html>
```